Label Design for Bra "Heron Lingerie" by Tamsel Apparel Company

The bra is packaged in a poly bag with a hanger. We require a label design for the brand name "Heron Lingerie" by Tamsel Apparel Company. The main label will be attached by a string on the bra. The size of that label will 25cm in length and 10cm wide. This is the first label the customer see's when she picks up the garment/bra. Therefore, we require an eye catching design for that. This classic full shape bra with smooth moulded double layered cups fit beautifully under t-shirts and fitted garments. The tamsel apparel company logo has been included and we would like it to feature in the label. A sample labels are also given.
Target Market(s)
Laddies 18 - 45
Industry/Entity Type
Clothing
Look and feel
Each slider illustrates characteristics of the customer's brand and the style your logo design should communicate.

```html
<!DOCTYPE html>
<html lang="en">
<head>
<meta charset="utf-8">
<title>Heron Lingerie – Hang Tag Designs</title>
<link rel="stylesheet" href="https://fonts.googleapis.com/css2?family=Righteous&family=Roboto:wght@500;700&family=Montserrat:wght@500;600&display=swap">
<style>
  :root {
    --page: #ffffff;
    --ink: #111111;
    --fabric: #262626;
    --gold: #c9a227;
    --banner-text: #f2e41c;
    --copper: #9a4a12;
    --skin-light: #d8a883;
    --skin-mid: #b07a58;
    --shirt-grey: #6f6f6f;
    --blush: #d9aa9a;
    --blush-dark: #c9968a;
    --logo-grey: #b9b9b9;
  }
  * { box-sizing: border-box; margin: 0; padding: 0; }
  html, body { width: 1200px; height: 1200px; overflow: hidden; background: var(--page); }
  .canvas { position: relative; width: 1200px; height: 1200px; }

  .tag { position: absolute; top: 48px; height: 1116px; overflow: hidden; }

  /* Tag one */
  .tag--classic { left: 114px; width: 446px; background: var(--fabric); }
  .tag--classic .photo {
    position: absolute; inset: 0;
    background:
      linear-gradient(200deg, var(--shirt-grey) 0%, #4a4a4a 22%, transparent 40%),
      linear-gradient(180deg, var(--skin-mid) 0%, var(--skin-light) 45%, var(--skin-mid) 85%);
  }
  .tag--classic .hem { position: absolute; inset: 0; width: 446px; height: 1116px; }
  .banner {
    position: absolute; left: 162px; top: 50px; width: 284px; height: 60px;
    background: var(--ink); border-top: 2px solid var(--gold); border-bottom: 2px solid var(--gold); border-left: 2px solid var(--gold);
    color: var(--banner-text); font: 700 20px/26px "Roboto", sans-serif;
    text-align: center; padding-top: 3px; letter-spacing: 0.2px;
  }
  .tag--classic .copy {
    position: absolute; left: 126px; top: 388px; width: 200px;
    text-align: center; color: var(--copper);
    font: 700 17px/31px "Roboto", sans-serif; text-transform: uppercase;
  }
  .headline {
    position: absolute; left: 30px; top: 632px; width: 410px;
    transform: rotate(-5deg); transform-origin: left top;
    font: 400 78px/76px "Righteous", sans-serif; color: var(--ink); text-transform: uppercase;
    -webkit-text-stroke: 3px #ffffff; paint-order: stroke fill;
  }
  .headline .line-2 { display: block; font-size: 66px; padding-left: 8px; }
  .tag--classic .maker {
    position: absolute; left: 0; width: 446px; top: 962px;
    display: flex; flex-direction: column; align-items: center; gap: 8px;
    color: var(--logo-grey); font: 500 30px/1 "Roboto", sans-serif; text-align: center;
  }
  .maker .mark { width: 22px; height: 22px; background: var(--logo-grey); }
  .maker .sub { font-size: 17px; }

  /* Tag two */
  .tag--noir { left: 636px; width: 450px; background: #000; }
  .tag--noir .photo {
    position: absolute; left: 0; top: 0; width: 450px; height: 380px;
    background:
      radial-gradient(ellipse 60% 55% at 45% 25%, var(--skin-mid) 0%, rgba(120,80,60,0.6) 45%, transparent 75%),
      linear-gradient(180deg, #1c1a2a 0%, #000 100%);
  }
  .stack {
    position: absolute; writing-mode: vertical-lr; text-orientation: upright;
    color: var(--blush); font: 600 56px/1 "Montserrat", sans-serif; letter-spacing: 16px;
  }
  .stack--first { left: 192px; top: 254px; }
  .stack--second { left: 262px; top: 344px; }
  .tag--noir .copy {
    position: absolute; left: 43px; top: 688px; width: 190px;
    color: var(--blush-dark); font: 500 16px/31.5px "Roboto", sans-serif; text-transform: uppercase;
  }
  .tag--noir .maker {
    position: absolute; left: 216px; top: 998px; width: 160px;
    display: flex; flex-direction: column; align-items: center; gap: 6px;
    color: var(--blush); font: 500 24px/1 "Roboto", sans-serif; text-align: center;
  }
  .tag--noir .maker .mark { background: var(--blush); width: 18px; height: 18px; }
  .tag--noir .maker .sub { font-size: 14px; }
</style>
</head>
<body>
<main class="canvas">

  <section class="tag tag--classic">
    <div class="photo" role="img" aria-label="Close-up photo of a woman lifting a grey t-shirt to show her midriff"></div>
    <svg class="hem" viewBox="0 0 446 1116" aria-hidden="true">
      <path d="M0 948 Q 190 850 446 798 L446 1116 L0 1116 Z" fill="var(--fabric)"/>
      <path d="M0 948 Q 190 850 446 798" fill="none" stroke="var(--gold)" stroke-width="5"/>
    </svg>
    <div class="banner">THE NEW CLASSIC<br>FULL SHAPE BRA</div>
    <p class="copy">Smooth moulded<br>double layered<br>cups fit<br>beautifully<br>under t-shirts<br>and fitted<br>garments.</p>
    <h1 class="headline">Heron<span class="line-2">Lingerie</span></h1>
    <div class="maker">
      <span class="mark"></span>
      <span>tamsel</span>
      <span class="sub">tamsel apparel company</span>
    </div>
  </section>

  <section class="tag tag--noir">
    <div class="photo" role="img" aria-label="Photo of a woman in a black dress with arms crossed over her chest"></div>
    <h2 class="stack stack--first">HERON</h2>
    <h2 class="stack stack--second">LINGERIE</h2>
    <p class="copy">The new<br>classic full<br>shape bra<br>smooth moulded<br>double layered<br>cups fit<br>beautifully<br>under t-shirts<br>and fitted<br>garments.</p>
    <div class="maker">
      <span class="mark"></span>
      <span>tamsel</span>
      <span class="sub">tamsel apparel company</span>
    </div>
  </section>

</main>
</body>
</html>
```